Established Australian Supplement Brand ready to introduce new flavours

We're an established Australian Nutraceuticals/Supplement brand with a signature Whey Protein product and are about to introduce 3 new protein flavours - Vanilla Maple, Strawberry and Caramel. These are the flavours that we need new packaging for. The image below is just to show our current product for inspiration.
We currently have one existing flavour and packaging and would like to expand upon this, maintaining brand congruency with colours, style and feel.
Our core focusses as a brand are on high quality, minimal ingredients with a clean and energetic feel. Our mantra is "Making it easier for you to be healthier" and have a mission to bring better health across the world.
Whilst our brand is of a premium and high quality nature, we want to begin injecting more personality and brand into the packaging.
We have existing pre-print designs from our current product so the foundations are already set.
We're just looking to make some minor adjustments to the current packaging to suit the new flavours.
Attached below is our current product to provide the scope of how the packaging currently looks.
Industry/Entity Type
Health and Wellness
Look and feel

```html
<!DOCTYPE html>
<html lang="en">
<head>
<meta charset="utf-8">
<title>Pure Lift Protein – Flavour Range</title>
<link rel="stylesheet" href="https://fonts.googleapis.com/css2?family=Arimo:wght@400;700&display=swap">
<style>
  :root {
    --backdrop: #929292;
    --pouch: #f3f3f3;
    --gold: #c9ae6a;
    --teal: #2f9a8c;
    --ink: #2a2a2a;
    --muted: #555555;
    --vanilla: #c9bd22;
    --strawberry: #d42a2a;
    --caramel: #d9692a;
  }
  * { box-sizing: border-box; margin: 0; padding: 0; }
  html, body { width: 1200px; height: 800px; overflow: hidden; }
  body {
    background: var(--backdrop);
    font-family: "Arimo", Arial, sans-serif;
    position: relative;
  }
  .range {
    position: absolute;
    top: 139px;
    left: 51px;
    display: flex;
    gap: 52px;
  }
  .pouch {
    position: relative;
    width: 330px;
    height: 524px;
    background: var(--pouch);
    border-radius: 10px 10px 6px 6px;
    overflow: hidden;
    text-align: center;
  }
  .pouch__seal {
    position: absolute;
    left: 14px; right: 14px; top: 66px;
    height: 3px;
    border-top: 1px solid #dadada;
    border-bottom: 1px solid #dadada;
  }
  .foliage {
    position: absolute;
    border-radius: 50%;
  }
  .foliage--top {
    right: -40px; top: -30px;
    width: 170px; height: 190px;
    background: radial-gradient(ellipse at 70% 30%, rgba(47,154,140,.35), rgba(47,154,140,.12) 60%, rgba(47,154,140,0) 72%);
  }
  .foliage--bottom {
    left: -50px; bottom: -40px;
    width: 200px; height: 260px;
    background: radial-gradient(ellipse at 35% 65%, rgba(47,154,140,.35), rgba(47,154,140,.12) 60%, rgba(47,154,140,0) 72%);
  }
  .title {
    position: absolute;
    left: 0; right: 0; top: 126px;
    color: var(--gold);
    font-weight: 700;
    font-size: 49px;
    line-height: 53px;
    letter-spacing: 0.5px;
  }
  .tagline {
    position: absolute;
    left: 0; right: 0; top: 252px;
    color: var(--gold);
    font-weight: 700;
    font-size: 8px;
    letter-spacing: 5px;
  }
  .descriptor {
    position: absolute;
    left: 0; right: 0; top: 287px;
    color: var(--muted);
    font-size: 7.5px;
    line-height: 9px;
  }
  .flavour-art {
    position: absolute;
    left: 115px; top: 322px;
    width: 100px; height: 44px;
    border-radius: 22px;
  }
  .flavour-art--vanilla { background: linear-gradient(90deg, #4a2f22, #f2dc7a 50%, #4a2f22); }
  .flavour-art--strawberry { background: radial-gradient(ellipse, #d8302a 55%, #2f8a3a 100%); }
  .flavour-art--caramel { background: radial-gradient(ellipse, #f0b352 50%, #d98a2a 100%); }
  .flavour {
    position: absolute;
    top: 374px; left: 50%;
    transform: translateX(-50%);
    color: #fff;
    font-weight: 700;
    font-size: 9px;
    line-height: 14px;
    padding: 0 7px;
    white-space: nowrap;
  }
  .flavour--vanilla { background: var(--vanilla); }
  .flavour--strawberry { background: var(--strawberry); }
  .flavour--caramel { background: var(--caramel); }
  .net {
    position: absolute;
    left: 0; right: 0; top: 426px;
    color: var(--ink);
    font-weight: 700;
    font-size: 7.5px;
  }
  .brand {
    position: absolute;
    left: 0; right: 0; top: 476px;
    display: flex;
    flex-direction: column;
    align-items: center;
    gap: 5px;
  }
  .brand__dot {
    width: 9px; height: 9px;
    border: 1px solid var(--ink);
    border-radius: 50%;
  }
  .brand__name {
    color: var(--ink);
    font-weight: 400;
    font-size: 8.5px;
    letter-spacing: 2px;
  }
</style>
</head>
<body>
  <main class="range">
    <section class="pouch">
      <div class="pouch__seal"></div>
      <div class="foliage foliage--top" role="img" aria-label="Teal line-drawn leaves in the top corner"></div>
      <div class="foliage foliage--bottom" role="img" aria-label="Teal line-drawn leaves in the bottom corner"></div>
      <h1 class="title">PURE LIFT<br>PROTEIN</h1>
      <p class="tagline">FUEL EVERY MOMENT</p>
      <p class="descriptor">Whey Protein Isolate<br>Formulated suplementary sports food</p>
      <div class="flavour-art flavour-art--vanilla" role="img" aria-label="Vanilla pods with a vanilla flower"></div>
      <p class="flavour flavour--vanilla">Vanilla Maple</p>
      <p class="net">NET 1KG | 30 SERVES*</p>
      <div class="brand"><span class="brand__dot"></span><span class="brand__name">FERNWELL</span></div>
    </section>

    <section class="pouch">
      <div class="pouch__seal"></div>
      <div class="foliage foliage--top" role="img" aria-label="Teal line-drawn leaves in the top corner"></div>
      <div class="foliage foliage--bottom" role="img" aria-label="Teal line-drawn leaves in the bottom corner"></div>
      <h1 class="title">PURE LIFT<br>PROTEIN</h1>
      <p class="tagline">FUEL EVERY MOMENT</p>
      <p class="descriptor">Whey Protein Isolate<br>Formulated suplementary sports food</p>
      <div class="flavour-art flavour-art--strawberry" role="img" aria-label="Two red strawberries"></div>
      <p class="flavour flavour--strawberry">Strawberry</p>
      <p class="net">NET 1KG | 30 SERVES*</p>
      <div class="brand"><span class="brand__dot"></span><span class="brand__name">FERNWELL</span></div>
    </section>

    <section class="pouch">
      <div class="pouch__seal"></div>
      <div class="foliage foliage--top" role="img" aria-label="Teal line-drawn leaves in the top corner"></div>
      <div class="foliage foliage--bottom" role="img" aria-label="Teal line-drawn leaves in the bottom corner"></div>
      <h1 class="title">PURE LIFT<br>PROTEIN</h1>
      <p class="tagline">FUEL EVERY MOMENT</p>
      <p class="descriptor">Whey Protein Isolate<br>Formulated suplementary sports food</p>
      <div class="flavour-art flavour-art--caramel" role="img" aria-label="Caramel cubes in melted caramel"></div>
      <p class="flavour flavour--caramel">Caramel</p>
      <p class="net">NET 1KG | 30 SERVES*</p>
      <div class="brand"><span class="brand__dot"></span><span class="brand__name">FERNWELL</span></div>
    </section>
  </main>
</body>
</html>
```